Project Managers Business card design

We need business cards for our Project Managers based in Sydney for our business name Korbet Pty Ltd. We project manage property improvements and infrastructure Assets. We provide asset owners Project Management services from original concept, management of architectural and engineering designs, call and select construction tenders, and manage the Asset operational life cycle to conclusion and removal. We are experienced in feasibility studies, risk assessments, quality control, safety control, environmental analysis. We are specialist in Aged Care and Child Care Services. We can provide asset reviewing checklists, asset inspections, contract cost and contract assessments, dispute resolution services and articles and books on safely working and living in environments subject to analysis. the design colours should be queensland marone and NSW sky blue.

Industry/Entity Type

Construction

Contact Information for Business Card

Gavin Trelowe (Mb 0412 847 391), Dennis Marquay (Mb 0438 216 074), Luke Benhadda,(Mb 0421 963 158)
E: all business cards: korbet@fernmail.example
Office phone number (02) 9482 3165
Address
Level 1 Halyard House
47 Wexford Lane, Parramatta
Web: projectmanagers@worksleadsbykorbet.example (to be checked on Printlyne web draft)

```html
<!DOCTYPE html>
<html lang="en">
<head>
<meta charset="utf-8">
<title>Korbet Pty Ltd — Project Manager Business Card</title>
<link rel="stylesheet" href="https://fonts.googleapis.com/css2?family=Saira:ital,wght@1,800&family=Arimo:wght@400&display=swap">
<style>
  :root {
    --backdrop: #3a3b3d;
    --card: #24272c;
    --card-edge: #1d2024;
    --ink: #16181b;
    --ink-soft: #1a1c20;
    --emboss-light: rgba(255, 255, 255, 0.07);
    --emboss-dark: rgba(0, 0, 0, 0.55);
  }
  * { margin: 0; padding: 0; box-sizing: border-box; }
  html, body {
    width: 1200px;
    height: 621px;
    overflow: hidden;
    background: var(--backdrop);
  }
  .canvas {
    position: relative;
    width: 1200px;
    height: 621px;
    background: var(--backdrop);
  }
  .card {
    position: absolute;
    top: 166px;
    width: 505px;
    height: 286px;
    background: var(--card);
    border: 1px solid var(--card-edge);
    box-shadow: 0 4px 12px rgba(0, 0, 0, 0.45);
    text-align: center;
  }
  .card--front { left: 60px; }
  .card--back { left: 628px; }
  .card__name {
    position: absolute;
    left: 0;
    right: 0;
    font-family: "Saira", "Arial Black", sans-serif;
    font-style: italic;
    font-weight: 800;
    font-size: 35px;
    letter-spacing: 1px;
    line-height: 1;
    color: var(--ink);
    text-shadow: 1px 1px 0 var(--emboss-light), -1px -1px 1px var(--emboss-dark);
  }
  .card--front .card__name { top: 114px; }
  .card--back .card__name { top: 50px; }
  .card__title {
    position: absolute;
    left: 0;
    right: 0;
    top: 153px;
    font-family: "Arimo", Arial, sans-serif;
    font-size: 15px;
    color: var(--ink-soft);
    text-shadow: 0 1px 0 var(--emboss-light);
  }
  .contact {
    position: absolute;
    left: 0;
    right: 0;
    top: 134px;
    list-style: none;
    font-family: "Arimo", Arial, sans-serif;
    font-size: 13.5px;
    line-height: 22px;
    letter-spacing: 0.3px;
    color: var(--ink-soft);
    text-shadow: 0 1px 0 var(--emboss-light);
  }
</style>
</head>
<body>
  <main class="canvas">
    <section class="card card--front" aria-label="Card front">
      <h1 class="card__name">Gavin Trelowe</h1>
      <p class="card__title">project manager</p>
    </section>
    <section class="card card--back" aria-label="Card back">
      <h2 class="card__name">Gavin Trelowe</h2>
      <ul class="contact">
        <li class="contact__mobile">M 0412 847 391</li>
        <li class="contact__phone">P (02) 9482 3165</li>
        <li class="contact__email">E korbet@fernmail.example</li>
        <li class="contact__web">W www.worksleadsbykorbet.example</li>
        <li class="contact__address">Level 1 Halyard House 47 Wexford Lane, Parramatta</li>
      </ul>
    </section>
  </main>
</body>
</html>
```